Premium men's gut health supplement needs a bottle label designed

We’re velnora - a premium men’s wellness brand focused on gut health. Our first product is a high-quality daily supplement designed to support digestion, regularity, and internal cleanliness. Backed by science and tailored for modern lifestyles, velnora is crafted in the UK and proudly LGBT-owned. It aims to resolve intimacy problems that gay men may experience due to poor digestion but also does not exclude any other orientation - other men may use it simply to improve their digestion.

velnora is for health-conscious men who value science-backed supplements and want to feel confident from the inside out. Many of our early adopters will be gay and bisexual men who prioritise gut health as part of their self-care, sexual, and hygiene routine, though the product is equally effective and appealing to anyone seeking premium digestive support.

The product is premium the target customer is male, not specific to one location but primary markets will be US, UK and EU.

I’d like a supplement bottle designed for velnora, our premium men’s gut health brand. The focus should be clean, slightly clinical, and minimal - inspired by brands like Quelrin and Darvo. The key element is the wordmark (velnora) on the front, with no additional logo or icon. Lowercase text and a strong, contemporary font are preferred.

The bottle should be aesthetically pleasing so that people are proud to display it on their shelf, instead of hiding it in a cupboard (like Quelrin, darvo, Pia Venturek, Morvanel etc)

Avoid anything that shows the product as being for LGBT, e.g., no rainbows, men holding hands etc.

The design should be premium, minimalist and not be busy or overwhelming.

I have uploaded a file called "Bottle" to give an idea of the type of container, but please ignore the colours and change as you see fit. This is just for reference for the type of bottle we'll use - all colours are customisable.

I have also uploaded some images for "style" reference, e.g., darvo, quelrin, pia venturek, etc for inspiration.

```html
<!DOCTYPE html>
<html lang="en">
<head>
<meta charset="utf-8">
<title>Velnora – Bottle Label</title>
<link rel="stylesheet" href="https://fonts.googleapis.com/css2?family=Marcellus&family=Jura:wght@500&display=swap">
<style>
  :root {
    --backdrop: #e4e4e4;
    --label-black: #1c1c1d;
    --label-sheen: #2a2a2b;
    --silver: #e6e6e6;
    --soft-white: #d8d8d8;
    --accent-blue: #2ab3e6;
  }
  html, body {
    margin: 0;
    padding: 0;
    width: 1200px;
    height: 1200px;
    overflow: hidden;
    background: var(--backdrop);
  }
  .canvas {
    position: relative;
    width: 1200px;
    height: 1200px;
    background: var(--backdrop);
  }
  .label {
    position: absolute;
    left: 200px;
    top: 100px;
    width: 800px;
    height: 1000px;
    background: linear-gradient(100deg, var(--label-black) 0%, var(--label-sheen) 45%, var(--label-black) 100%);
    text-align: center;
  }
  .wordmark {
    position: absolute;
    top: 150px;
    left: 0;
    right: 0;
    margin: 0;
    font-family: "Marcellus", serif;
    font-weight: 400;
    font-size: 150px;
    line-height: 1;
    color: var(--silver);
  }
  .descriptor {
    position: absolute;
    top: 500px;
    left: 0;
    right: 0;
    margin: 0;
    font-family: "Jura", sans-serif;
    font-weight: 500;
    font-size: 46px;
    line-height: 1.2;
    letter-spacing: 0.06em;
    color: var(--soft-white);
    text-transform: uppercase;
  }
  .count {
    position: absolute;
    top: 880px;
    left: 0;
    right: 0;
    margin: 0;
    font-family: "Jura", sans-serif;
    font-weight: 500;
    font-size: 28px;
    letter-spacing: 0.12em;
    color: var(--soft-white);
  }
  .accent-rule {
    position: absolute;
    top: 922px;
    left: 0;
    width: 800px;
    height: 6px;
    background: var(--accent-blue);
  }
  .category {
    position: absolute;
    top: 948px;
    left: 0;
    right: 0;
    margin: 0;
    font-family: "Jura", sans-serif;
    font-weight: 500;
    font-size: 22px;
    letter-spacing: 0.1em;
    color: var(--soft-white);
  }
</style>
</head>
<body>
  <main class="canvas">
    <section class="label">
      <h1 class="wordmark">Velnora</h1>
      <p class="descriptor">Premium Men’s Gut<br>Health Supplement</p>
      <p class="count">90 VEGAN CAPSULES</p>
      <div class="accent-rule"></div>
      <p class="category">FOOD SUPPLEMENT</p>
    </section>
  </main>
</body>
</html>
```